LatAm Power Generation PPT - Corporate office in Houston, TX - USA

Here's our website: norvalpower.com. We are Norval Power Holdings LLC. We are a small corporate office that manages power generation assets located in Latin America. We are pro clean energy, including thermal generation as long as it is gas-fired equipment (no coal-fired plants in our portfolio). Brazil is the first country where we have a presence in and we intend to grow significantly in the region in the next few years. We report to a private equity in the US, that is a co-investor. We would like a formal, elegant and detailed presentation for Board meetings, Budget reviews, Investment proposals, etc.
We have a logo/business cards just created with a ArtFolkHub designer, which are uploaded.
Updates

Everyone: Focus of our core business is conventional energy, primarily thermal energy (except Coal). All the same, renewable energy is relevant, just not the sole objective. Thanks for participating!

```html
<!DOCTYPE html>
<html lang="en">
<head>
<meta charset="utf-8">
<title>Norval Power – Presentation Template Overview</title>
<link href="https://fonts.googleapis.com/css2?family=Lato:wght@300;400;700;900&display=swap" rel="stylesheet">
<style>
:root{
  --navy:#1b2266;
  --green:#3db33a;
  --green-deep:#1f8a2c;
  --ink:#3a3a3a;
  --muted:#8a8a8a;
  --stage:#eceeea;
  --paper:#ffffff;
  --pill:#4a4a4a;
}
*{box-sizing:border-box;margin:0;padding:0}
html,body{width:1200px;height:526px;overflow:hidden;background:var(--stage);font-family:'Lato',sans-serif}
.deck{position:relative;width:1200px;height:526px}
.slide{position:absolute;width:284px;height:160px;background:var(--paper);overflow:hidden;box-shadow:0 2px 6px rgba(0,0,0,.18)}
.c1{left:18px}.c2{left:322px}.c3{left:623px}.c4{left:914px}
.r1{top:6px}.r2{top:178px}.r3{top:350px}
.brand{position:absolute;right:10px;top:9px;display:flex;align-items:center;gap:2px;font-size:6px;font-weight:700;color:var(--green-deep);z-index:3}
.brand i{width:7px;height:7px;border-radius:50%;background:var(--green);display:block}
.title{position:absolute;left:14px;top:19px;font-size:9.5px;font-weight:400;color:var(--navy);letter-spacing:-.2px;line-height:1}
.sub{position:absolute;font-size:2.6px;color:var(--navy)}
.p{font-size:2.7px;line-height:1.45;color:var(--muted);text-align:justify}
.photo{position:absolute;background:linear-gradient(160deg,#6b6f78,#2d2f35)}
.photo.tint{background:linear-gradient(160deg,#7ccc6e,#3a9c3a)}
.photo.blue{background:linear-gradient(160deg,#3f7c86,#12262b)}
.pill{position:absolute;height:6px;background:var(--pill);color:#fff;font-size:2.6px;font-weight:700;display:flex;align-items:center;justify-content:center;border-radius:1px}
.foot{position:absolute;bottom:8px;font-size:2px;letter-spacing:.6px;color:#b0b0b0}
.edge{position:absolute;inset:0;z-index:1}
.h2{font-size:6.5px;color:#333;line-height:1.15;font-weight:400}
.bar{height:1.2px;background:#ddd;position:relative;margin:1px 0 4px}
.bar b{position:absolute;left:0;top:0;height:1.2px;background:#222}
.bar span{position:absolute;right:-12px;top:-1.5px;font-size:2.4px;color:var(--navy)}
.bl{font-size:2.4px;color:var(--navy)}
.tile{position:absolute;top:56px;width:51px;height:104px;background:linear-gradient(180deg,#cfcfcf,#5d5d5d);color:#fff;text-align:center}
.tile h4{font-size:4px;font-weight:400;margin-top:52px}
.tile p{font-size:2.6px;line-height:1.3;padding:2px 4px}
</style>
</head>
<body>
<main class="deck">

<!-- Row 1 -->
<section class="slide c1 r1">
  <div class="brand"><i></i>Norval Power</div>
  <h2 class="title" style="top:24px;font-size:8.5px">TEAM'S BACKGROUND</h2>
  <p class="p" style="position:absolute;left:14px;top:36px;width:256px">Our management team has a proven track record of success in the energy sector and in the region. Most recently, our team was part of Meridian Grid International's senior executive group, a revenue platform that became the largest private company in its space, with power plants, distribution customers and a broad network of gas transportation pipelines among other energy assets. The team developed a thorough knowledge of each company's growth and executed a divestiture strategy that achieved significant returns for shareholders. Norval Power's management team brings in-depth knowledge, understanding, know-how and experience of the relevant markets and assets, and has access to a broad group of professionals with track record in the industry to support the platform's growth efforts in Latin America.</p>
  <div class="photo" role="img" aria-label="Portrait of Marco L. Arriaga" style="left:14px;top:75px;width:54px;height:54px"></div>
  <div class="photo" role="img" aria-label="Portrait of Daniel R. Ostrand" style="left:81px;top:75px;width:54px;height:54px"></div>
  <div class="photo tint" role="img" aria-label="Portrait placeholder for Pablo Serrano" style="left:149px;top:75px;width:54px;height:54px"></div>
  <div class="photo tint" role="img" aria-label="Portrait placeholder for Andres Quintero" style="left:216px;top:75px;width:54px;height:54px"></div>
  <div class="pill" style="left:20px;top:132px;width:42px">Marco L. Arriaga</div>
  <div class="pill" style="left:87px;top:132px;width:42px">Daniel R. Ostrand</div>
  <div class="pill" style="left:155px;top:132px;width:42px">Pablo Serrano</div>
  <div class="pill" style="left:222px;top:132px;width:42px">Andres Quintero</div>
  <div class="foot" style="left:36px">NORVAL POWER</div><div class="foot" style="right:36px">www.norvalpower.com</div>
</section>

<section class="slide c2 r1">
  <div class="photo" role="img" aria-label="Portrait of Daniel R. Ostrand in front of a bookshelf" style="left:142px;top:20px;width:130px;height:126px"></div>
  <div style="position:absolute;left:24px;top:32px;width:140px;height:99px;background:var(--navy);padding:7px 12px;z-index:2">
    <h3 style="color:#fff;font-size:9px;font-weight:400;margin-bottom:5px">Daniel R. Ostrand</h3>
    <p class="p" style="color:#e6e8f5;font-size:3.6px;line-height:1.4">Attorney/Executive Manager with more than 12 years of experience in the power sector in South and Central America and the Caribbean, first working with Altavia Power, and since 2007 with Meridian Grid International, where he served as Regional General Counsel for Central America and the Caribbean. He has extensive experience in cross border transactions, M&amp;A, financing, asset management and business development. He holds an LLM degree from Whitmore School of Law (US) and an MBA degree from Costa Verde School of Management (US) and Lindquist Business School.</p>
  </div>
</section>

<section class="slide c3 r1">
  <div style="position:absolute;left:0;top:0;width:90px;height:160px;background:var(--green)"></div>
  <div class="brand"><i></i>Norval Power</div>
  <h2 class="title" style="left:54px;top:24px;font-size:8.5px">MEET OUR PRINCIPALS</h2>
  <p class="p" style="position:absolute;left:54px;top:35px;width:130px;font-size:2.4px">Simply dummy text of the printing and typesetting industry when an unknown printer took a galley of type and scrambled.</p>
  <div class="photo" role="img" aria-label="Portrait of Marco L. Arriaga" style="left:35px;top:55px;width:67px;height:67px"></div>
  <h3 style="position:absolute;left:127px;top:56px;font-size:8px;font-weight:400;color:var(--navy)">Marco L. Arriaga</h3>
  <p class="p" style="position:absolute;left:127px;top:69px;width:132px;font-size:2.8px">Executive Manager with over 20 years of global energy experience in both regulated and unregulated markets in Latin America, Europe and Asia. Mr. Arriaga was last Meridian Grid International's CEO, responsible for all aspects of an organization owning and operating assets in twenty countries in Asia, Latin America and Europe, spanning through power generation, electricity and gas distribution utilities, gas transportation, and fuel retail. Previously, he worked for Corvane and for Ibercal. He was board member in recognized energy companies across the region. He holds an MBA degree from Ashgrove Business School.</p>
  <div class="foot" style="left:36px;color:#e8f5e4">NORVAL POWER</div><div class="foot" style="right:36px">www.norvalpower.com</div>
</section>

<section class="slide c4 r1">
  <div class="brand"><i></i>Norval Power</div>
  <div style="position:absolute;left:20px;top:43px;width:12px;height:1.5px;background:linear-gradient(90deg,var(--green) 50%,var(--navy) 50%)"></div>
  <h2 style="position:absolute;left:20px;top:50px;font-size:7.5px;font-weight:400;color:var(--navy);line-height:1.2">MEET THE<br>NORVAL POWER TEAM</h2>
  <p class="p" style="position:absolute;left:20px;top:75px;width:60px;font-size:2.4px">Simply dummy text of the printing and typesetting industry when an unknown printer type.</p>
  <p class="p" style="position:absolute;left:20px;top:92px;width:64px;font-size:2.4px">Lorem ipsum dolor sit amet, consectetur adipiscing elit, sed do eiusmod tempor incididunt ut labore et dolore magna aliqua. Ut enim ad minim veniam, quis nostrud exercitation ullamco laboris nisi ut aliquip.</p>
  <div style="position:absolute;left:110px;top:28px;display:grid;grid-template-columns:repeat(4,33px);column-gap:8.5px;row-gap:25px">
    <div class="photo blue" role="img" aria-label="Team member portrait" style="position:relative;height:33px"></div>
    <div class="photo blue" role="img" aria-label="Team member portrait" style="position:relative;height:33px"></div>
    <div class="photo blue" role="img" aria-label="Team member portrait" style="position:relative;height:33px"></div>
    <div class="photo blue" role="img" aria-label="Team member portrait" style="position:relative;height:33px"></div>
    <div class="photo blue" role="img" aria-label="Team member portrait" style="position:relative;height:33px"></div>
    <div class="photo blue" role="img" aria-label="Team member portrait" style="position:relative;height:33px"></div>
    <div class="photo blue" role="img" aria-label="Team member portrait" style="position:relative;height:33px"></div>
    <div class="photo blue" role="img" aria-label="Team member portrait" style="position:relative;height:33px"></div>
  </div>
  <div style="position:absolute;left:110px;top:63px;display:grid;grid-template-columns:repeat(4,33px);column-gap:8.5px;row-gap:52px;text-align:center;font-size:2.6px;font-weight:700;color:var(--navy)">
    <span>JORDAN ELLERY</span><span>JORDAN ELLERY</span><span>JORDAN ELLERY</span><span>JORDAN ELLERY</span>
    <span>JORDAN ELLERY</span><span>JORDAN ELLERY</span><span>JORDAN ELLERY</span><span>JORDAN ELLERY</span>
  </div>
  <div class="foot" style="left:36px">NORVAL POWER</div><div class="foot" style="right:36px">www.norvalpower.com</div>
</section>

<!-- Row 2 -->
<section class="slide c1 r2">
  <svg class="edge" viewBox="0 0 284 160" aria-hidden="true">
    <path d="M0 0H9C4 50 4 110 14 160H0Z" fill="var(--navy)"/>
    <path d="M9 0C4 50 4 110 14 160H26C12 120 8 60 9 0Z" fill="var(--green)"/>
  </svg>
  <div class="brand"><i></i>Norval Power</div>
  <h2 class="title" style="left:26px">OVERVIEW 4 DESCRIPTION</h2>
  <p class="sub" style="left:26px;top:30px">Lorem Ipsum available, but the majority have suffered alteration.</p>
  <div style="position:absolute;left:26px;top:54px;width:244px">
    <p style="font-size:3.4px;font-weight:700;color:#222">✓ YOUR FIRST TITLE GOES HERE:</p>
    <p class="p" style="color:#555;margin-bottom:4px">Nulla varius vehicula augue, id placerat nisi luctus a. Suspendisse magna tellus, imperdiet id turpis in, gravida fermentum sem. Integer commodo pharetra dui a congue. Vivamus imperdiet id turpis in, gravida fermentum.</p>
    <p style="font-size:3.4px;font-weight:700;color:#222">✓ YOUR SECOND TITLE GOES HERE:</p>
    <p class="p" style="color:#555;margin-bottom:4px">Integer commodo pharetra dui a congue. Vivamus imperdiet id turpis in, gravida fermentum. Suspendisse magna. Nulla varius vehicula augue, id placerat nisi luctus a. Suspendisse magna tellus, imperdiet id turpis in, gravida fermentum sem.</p>
    <p style="font-size:3.4px;font-weight:700;color:#222">✓ YOUR THIRD TITLE GOES HERE:</p>
    <p class="p" style="color:#555;margin-bottom:4px">Nulla varius vehicula augue, id placerat nisi luctus a. Suspendisse magna tellus, imperdiet id turpis in, gravida fermentum sem. Integer commodo pharetra dui a congue. Vivamus imperdiet id turpis in, gravida fermentum.</p>
    <p style="font-size:3.4px;font-weight:700;color:#222">✓ YOUR FOURTH TITLE GOES HERE:</p>
    <p class="p" style="color:#555">Integer commodo pharetra dui a congue. Vivamus imperdiet id turpis in, gravida fermentum. Suspendisse magna. Nulla varius vehicula augue, id placerat nisi luctus a. Suspendisse magna tellus, imperdiet id turpis in, gravida fermentum sem.</p>
  </div>
</section>

<section class="slide c2 r2">
  <svg class="edge" viewBox="0 0 284 160" aria-hidden="true">
    <path d="M284 0H276C266 50 266 110 272 160H284Z" fill="var(--navy)"/>
    <path d="M276 0C266 50 266 110 272 160H262C256 110 258 50 276 0Z" fill="var(--green)"/>
  </svg>
  <div class="brand" style="right:18px"><i></i>Norval Power</div>
  <h2 class="title">OVERVIEW 3 ROWS</h2>
  <p class="sub" style="left:14px;top:30px">Lorem Ipsum available, but the majority have suffered alteration.</p>
  <p class="h2" style="position:absolute;left:14px;top:53px">There are many variations<br>of passages of Lorem Ipsum available</p>
  <div style="position:absolute;left:14px;top:74px;width:230px">
    <p class="p" style="color:#555;margin-bottom:5px">Lorem ipsum dolor sit amet, consectetur adipiscing elit. Donec mauris lorem, vestibulum ac rutrum id, suscipit in dui. Donec vitae dapibus tellus. Vestibulum nunc sem, finibus quis elementum ac, varius ac tellus. Nam faucibus faucibus venenatis. Donec nec arcu velit. Fusce viverra, dui vitae euismod mollis, tortor magna egestas nunc, et suscipit nunc ex quis nunc. Pellentesque habitant morbi tristique senectus et netus. Integer eget auctor nunc.</p>
    <p class="p" style="color:#555;margin-bottom:5px">Nulla efficitur urna et massa dapibus maximus. Maecenas sit amet risus pretium, sagittis dui ut, consectetur purus. Phasellus auctor consectetur arcu a consequat. Vestibulum congue sed orci efficitur finibus. Integer malesuada finibus ligula, aliquet lobortis nulla commodo vel.</p>
    <p class="p" style="color:#555">Nulla varius vehicula augue, id placerat nisi luctus a. Suspendisse magna tellus, imperdiet id turpis in, gravida fermentum sem. Integer commodo pharetra dui a congue. Vivamus in commodo dui. Nunc fringilla ex sapien, et laoreet erat pretium ultricies. In hac habitasse platea dictumst. Cum sociis natoque penatibus.</p>
  </div>
</section>

<section class="slide c3 r2">
  <svg class="edge" viewBox="0 0 284 160" aria-hidden="true">
    <path d="M284 0H276C266 50 266 110 272 160H284Z" fill="var(--navy)"/>
    <path d="M276 0C266 50 266 110 272 160H262C256 110 258 50 276 0Z" fill="var(--green)"/>
  </svg>
  <div class="brand" style="right:18px"><i></i>Norval Power</div>
  <h2 class="title">OVERVIEW 2 COLUMN</h2>
  <p class="sub" style="left:14px;top:30px">Lorem Ipsum available, but the majority have suffered alteration.</p>
  <p class="h2" style="position:absolute;left:14px;top:53px">There are many variations<br>of passages of Lorem Ipsum available</p>
  <div style="position:absolute;left:14px;top:78px;width:232px;display:grid;grid-template-columns:1fr 1fr;gap:10px">
    <div><p class="p" style="color:#555;margin-bottom:5px">Lorem ipsum dolor sit amet, consectetur adipiscing elit. Donec mauris lorem, vestibulum ac rutrum id, suscipit in dui. Donec vitae dapibus tellus. Vestibulum nunc sem, finibus quis elementum ac, varius ac tellus. Nam faucibus faucibus venenatis. Donec nec arcu velit. Fusce viverra, dui vitae euismod mollis, tortor magna egestas nunc, et suscipit nunc ex quis nunc. Pellentesque habitant morbi tristique senectus et netus et malesuada fames. Integer eget auctor nunc.</p>
    <p class="p" style="color:#555">Nulla efficitur urna et massa dapibus maximus. Maecenas sit amet risus pretium, sagittis dui ut, consectetur purus. Phasellus auctor consectetur.</p></div>
    <div><p class="p" style="color:#555">Arcu a consequat. Vestibulum congue sed orci efficitur finibus. Integer malesuada finibus ligula, aliquet lobortis nulla commodo vel. Nulla varius vehicula augue, id placerat nisi luctus a. Suspendisse magna tellus, imperdiet id turpis in, gravida fermentum sem. Integer commodo pharetra dui a congue. Vivamus in commodo dui. Nunc fringilla ex sapien, et laoreet erat pretium ultricies. In hac habitasse platea dictumst. Donec lacinia efficitur dictum. Cum sociis natoque penatibus et magnis dis parturient montes, nascetur ridiculus mus. Nam odio nulla, tempor a eleifend ut, dignissim.</p></div>
  </div>
</section>

<section class="slide c4 r2">
  <svg class="edge" viewBox="0 0 284 160" aria-hidden="true">
    <path d="M284 0H276C266 50 266 110 272 160H284Z" fill="var(--navy)"/>
    <path d="M276 0C266 50 266 110 272 160H262C256 110 258 50 276 0Z" fill="var(--green)"/>
  </svg>
  <div class="brand" style="right:18px"><i></i>Norval Power</div>
  <h2 class="title">OVERVIEW 3 COLUMN</h2>
  <p class="sub" style="left:14px;top:30px">Lorem Ipsum available, but the majority have suffered alteration.</p>
  <div style="position:absolute;left:14px;top:50px;width:238px;display:grid;grid-template-columns:1fr 1fr 1fr;gap:6px">
    <div><p class="p" style="color:#555;margin-bottom:5px">Lorem ipsum dolor sit amet, consectetur adipiscing elit. Donec mauris lorem, vestibulum ac rutrum id, suscipit in dui. Donec vitae dapibus tellus. Vestibulum nunc sem, finibus quis elementum ac, varius ac tellus. Nam faucibus faucibus venenatis. Donec nec arcu velit. Fusce viverra, dui vitae euismod mollis, tortor magna egestas nunc, et suscipit nunc ex quis nunc. Pellentesque habitant morbi tristique senectus et netus et malesuada fames ac turpis egestas. Integer eget auctor nunc.</p>
    <p class="p" style="color:#555">Nulla efficitur urna et massa dapibus maximus. Maecenas sit amet risus pretium, sagittis dui ut, consectetur purus. Phasellus auctor consectetur arcu a consequat. Vestibulum congue sed orci efficitur finibus.</p></div>
    <div><p class="p" style="color:#555;margin-bottom:5px">Aliquet lobortis nulla commodo vel. Nulla varius vehicula augue, id placerat nisi luctus a. Suspendisse magna tellus, imperdiet id turpis in, gravida fermentum sem. Integer commodo pharetra dui a congue. Vivamus in commodo dui. Nunc fringilla ex sapien, et laoreet erat pretium ultricies. In hac habitasse platea dictumst. Donec lacinia efficitur dictum. Cum sociis natoque penatibus et magnis dis parturient montes, nascetur ridiculus mus. Nam odio nulla, tempor a eleifend ut.</p>
    <p class="p" style="color:#555">Vestibulum nunc sem, finibus quis elementum ac.</p></div>
    <div><p class="p" style="color:#555;margin-bottom:5px">Varius ac tellus. Nam faucibus faucibus venenatis. Donec nec arcu velit. Fusce viverra, dui vitae euismod mollis, tortor magna egestas nunc, et suscipit nunc ex quis nunc. Nulla varius vehicula augue, id placerat nisi luctus a. Suspendisse magna tellus, imperdiet id turpis in, gravida fermentum sem. Integer commodo pharetra dui a congue.</p>
    <p class="p" style="color:#555">Vivamus in commodo dui. Nunc fringilla ex sapien, et laoreet erat pretium ultricies. In hac habitasse platea dictumst. Donec lacinia efficitur dictum. Nam odio nulla, tempor a eleifend ut, dignissim nec tellus.</p></div>
  </div>
</section>

<!-- Row 3 -->
<section class="slide c1 r3">
  <div class="brand"><i></i>Norval Power</div>
  <h2 class="title" style="left:19px">IMAGE WITH 2 COLUMN</h2>
  <p class="sub" style="left:19px;top:30px">Lorem Ipsum available, but the majority have suffered alteration.</p>
  <div role="img" aria-label="Photo of a high-voltage transmission tower at sunset" style="position:absolute;left:0;top:30px;width:78px;height:122px;background:linear-gradient(180deg,#c9d6e2,#b79a6a 70%,#8a6a3c)"></div>
  <div style="position:absolute;left:89px;top:48px;width:88px">
    <p class="h2" style="font-size:6.5px">The Best Presentation Layout with Two Columns</p>
    <p style="font-size:5px;color:#444;margin:3px 0 6px">Image and Description</p>
    <p class="p" style="color:var(--navy)">Lorem ipsum dolor sit amet, this placeholder text can be added on your instruction. A strong layout holds the text in place and keeps the reader focused on the key message. This standard defines an onerous contract as a contract in which the unavoidable costs of meeting the obligations under the contract exceed the economic benefits expected to be received under it. Continuing staff; marketing; investment in new systems and distribution networks. These expenditures relate to the future conduct of the business.</p>
  </div>
  <div style="position:absolute;left:181px;top:44px;width:88px">
    <p class="p" style="color:#555;margin-bottom:5px">Lorem ipsum dolor sit amet, this placeholder text can be added on your instruction. It is not simply random content as a contract in which the unavoidable costs of meeting the obligations under the contract exceed the economic benefits expected to be received under it. Continuing staff; marketing; investment in new systems and distribution networks. These expenditures relate to the future conduct of the business and are not lets is envisaged as part of the restructuring. The current warranty. Many contracts (for example, some routine purchase orders).</p>
    <p class="p" style="color:#555">Other contracts establish both rights and obligations for each of the contracting parties. Where events make such a contract onerous, the contract falls.</p>
  </div>
</section>

<section class="slide c2 r3">
  <div class="brand"><i></i>Norval Power</div>
  <div style="position:absolute;left:24px;top:24px;width:236px;height:114px;background:#efefef"></div>
  <div role="img" aria-label="Photo of wind turbines under a bright blue sky" style="position:absolute;left:0;top:34px;width:134px;height:96px;background:linear-gradient(180deg,#6fa9d8,#d5e6f3 60%,#9fb4a8)"></div>
  <h2 style="position:absolute;left:155px;top:45px;font-size:8.5px;font-weight:400;color:var(--navy)">OUR PROJECT ADVANCE</h2>
  <p class="p" style="position:absolute;left:155px;top:58px;width:100px;font-size:2.4px">Simply dummy text of the printing and typesetting industry when an unknown printer type specimen book unknown printer took a galley of type and scrambled.</p>
  <div style="position:absolute;left:155px;top:80px;width:72px">
    <p class="bl">MEET BUDGET</p><div class="bar"><b style="width:100%"></b><span>100%</span></div>
    <p class="bl">PROJECT ADVANCE</p><div class="bar"><b style="width:80%"></b><span>80%</span></div>
    <p class="bl">TIME SCHEDULE</p><div class="bar"><b style="width:60%"></b><span>60%</span></div>
    <p class="bl">MARKETING</p><div class="bar"><b style="width:85%;background:#ccc"></b><span>85%</span></div>
  </div>
  <div class="foot" style="left:36px">NORVAL POWER</div><div class="foot" style="right:36px">www.norvalpower.com</div>
</section>

<section class="slide c3 r3">
  <div class="brand"><i></i>Norval Power</div>
  <h2 class="title" style="left:30px;top:23px;font-size:8.5px">OUR SERVICES</h2>
  <p class="p" style="position:absolute;left:30px;top:34px;width:220px;font-size:3.2px;text-align:left">Simply dummy text of the printing and typesetting industry when an unknown printer type specimen book unknown printer took a galley of type and scrambled.</p>
  <div class="tile" role="img" aria-label="Grayscale photo of a transmission tower" style="left:30px"><h4>DEVELOPMENT</h4><p>Make a type specimen book unknown printer took a galley of type and scrambled it to make a type specimen book.</p></div>
  <div class="tile" role="img" aria-label="Grayscale photo of a wind turbine" style="left:87px"><h4>DESIGN</h4><p>Make a type specimen book unknown printer took a galley of type and scrambled it to make a type specimen book.</p></div>
  <div class="tile" role="img" aria-label="Grayscale photo of a construction site" style="left:144px"><h4>CONSTRUCTION</h4><p>Make a type specimen book unknown printer took a galley of type and scrambled it to make a type specimen book.</p></div>
  <div class="tile" role="img" aria-label="Grayscale photo of an industrial cooling plant" style="left:201px"><h4>MAINTENANCE</h4><p>Make a type specimen book unknown printer took a galley of type and scrambled it to make a type specimen book.</p></div>
</section>

<section class="slide c4 r3">
  <svg class="edge" viewBox="0 0 284 160" aria-hidden="true">
    <path d="M284 0H276C266 50 266 110 272 160H284Z" fill="var(--navy)"/>
    <path d="M276 0C266 50 266 110 272 160H262C256 110 258 50 276 0Z" fill="var(--green)"/>
  </svg>
  <div class="brand" style="right:18px"><i></i>Norval Power</div>
  <h2 class="title" style="left:26px;top:23px;font-size:8.5px">OUR PROJECTS</h2>
  <p class="p" style="position:absolute;left:26px;top:34px;width:225px;font-size:3.2px;text-align:left">Simply dummy text of the printing and typesetting industry when an unknown printer type specimen book unknown printer took a galley of type and scrambled. Simply dummy text of the printing and typesetting.</p>
  <div role="img" aria-label="Collage of transmission towers, solar panels, an industrial plant and a business meeting" style="position:absolute;left:26px;top:56px;width:228px;height:84px;background:linear-gradient(90deg,#c9b58a 0%,#8fb2d4 25%,#3c5f8c 50%,#7fa0b8 75%,#d8d8d8 100%)"></div>
  <div class="foot" style="left:36px">NORVAL POWER</div><div class="foot" style="right:36px">www.norvalpower.com</div>
</section>

</main>
</body>
</html>
```